Lumora Chiropractic & Acupuncture Business Cards

I need a business card design that feels elevated. I am open to any of the logo designs uploaded. We have two doctors so I'll need to be able to change out the names.

Information:
Marlena Quist D.C., Dipl. Ac. ASA
487 W 12th St, Ste 204
Fernhollow, OR 97390
lumoraclinic.example
541-555-0143
drmarlena@lumoraclinic.example
Updates

We have designs we like now, we are just trying to choose between top contenders. Thanks for your submissions!

Contact Information for Business Card

noted in description

Requirements
Must have
• ability to edit info if possible
Nice to have
• Please see our website lumoraclinic.example for our style and colors

```html
<!DOCTYPE html>
<html lang="en">
<head>
<meta charset="UTF-8">
<title>Lumora Chiropractic &amp; Acupuncture – Business Cards</title>
<link href="https://fonts.googleapis.com/css2?family=Playfair+Display:wght@400&display=swap" rel="stylesheet">
<style>
  :root {
    --navy: #333b4f;
    --cream: #f0f1ea;
    --sand: #d1c8be;
    --backdrop: #e8e8e8;
  }
  * { box-sizing: border-box; margin: 0; padding: 0; }
  html, body {
    width: 1200px;
    height: 1200px;
    overflow: hidden;
    background: var(--backdrop);
    font-family: "Playfair Display", Georgia, serif;
    color: var(--navy);
  }
  .sheet {
    position: relative;
    width: 1200px;
    height: 1200px;
  }
  .card {
    position: absolute;
    left: 140px;
    width: 920px;
    height: 511px;
    background: var(--cream);
    overflow: hidden;
  }
  .card--front { top: 69px; }
  .card--back { top: 620px; }

  /* Front */
  .brand {
    position: absolute;
    inset: 0;
    display: flex;
    flex-direction: column;
    align-items: center;
    justify-content: center;
    text-align: center;
  }
  .brand__name {
    font-size: 118px;
    font-weight: 400;
    line-height: 1;
    letter-spacing: 1px;
  }
  .brand__tagline {
    margin-top: 10px;
    font-size: 19px;
    font-weight: 400;
    letter-spacing: 1px;
    text-transform: uppercase;
  }

  /* Back */
  .back-art {
    position: absolute;
    inset: 0;
    width: 100%;
    height: 100%;
  }
  .doctor {
    position: absolute;
    left: 59px;
    top: 98px;
    white-space: nowrap;
  }
  .doctor__name {
    font-size: 40px;
    letter-spacing: 2px;
    text-transform: uppercase;
  }
  .doctor__credentials {
    font-size: 25px;
    letter-spacing: 1.5px;
    text-transform: uppercase;
  }
  .address {
    position: absolute;
    left: 60px;
    top: 160px;
    font-size: 16.5px;
    white-space: nowrap;
  }
  .divider {
    position: absolute;
    left: 60px;
    top: 205px;
    width: 408px;
    height: 2px;
    background: var(--navy);
  }
  .contact-list {
    position: absolute;
    left: 60px;
    top: 266px;
    list-style: none;
  }
  .contact-list__item {
    display: flex;
    align-items: center;
    gap: 14px;
    height: 28px;
    margin-bottom: 22px;
    font-size: 25px;
    white-space: nowrap;
  }
  .contact-list__icon {
    width: 28px;
    height: 28px;
    flex: none;
  }
</style>
</head>
<body>
<main class="sheet">

  <section class="card card--front">
    <div class="brand">
      <div class="brand__name">Lumora</div>
      <div class="brand__tagline">Chiropractic &amp; Acupuncture</div>
    </div>
  </section>

  <section class="card card--back">
    <svg class="back-art" viewBox="0 0 1165 648" preserveAspectRatio="none" aria-hidden="true">
      <path fill="var(--sand)" d="M835,0 C872,130 872,300 838,420 C818,482 797,522 770,568 C812,500 852,420 872,330 C892,220 882,100 855,0 Z"/>
      <path fill="var(--navy)" d="M877,0 C918,120 918,262 882,382 C842,500 792,580 723,648 L1165,648 L1165,0 Z"/>
      <ellipse cx="1025" cy="330" rx="102" ry="114" fill="var(--sand)"/>
      <ellipse cx="1025" cy="330" rx="96" ry="108" fill="none" stroke="var(--cream)" stroke-width="1.2"/>
    </svg>

    <div class="doctor">
      <span class="doctor__name">Marlena Quist</span>
      <span class="doctor__credentials">D.C., Dipl. Ac. ASA</span>
    </div>
    <div class="address">487 W 12th St, Ste 204, Fernhollow, OR 97390</div>
    <div class="divider"></div>

    <ul class="contact-list">
      <li class="contact-list__item">
        <svg class="contact-list__icon" viewBox="0 0 28 28" aria-hidden="true">
          <circle cx="14" cy="14" r="14" fill="var(--navy)"/>
          <path fill="#fff" d="M9.5 7.5 C10.5 7 11.3 7.4 11.7 8.3 L12.6 10.5 C12.9 11.2 12.7 11.8 12.1 12.3 L11.4 12.9 C12.2 14.6 13.4 15.8 15.1 16.6 L15.7 15.9 C16.2 15.3 16.8 15.1 17.5 15.4 L19.7 16.3 C20.6 16.7 21 17.5 20.5 18.5 C19.8 20 18.3 20.8 16.6 20.3 C12.6 19.1 8.9 15.4 7.7 11.4 C7.2 9.7 8 8.2 9.5 7.5 Z"/>
        </svg>
        <span>541-555-0143</span>
      </li>
      <li class="contact-list__item">
        <svg class="contact-list__icon" viewBox="0 0 28 28" aria-hidden="true">
          <circle cx="14" cy="14" r="14" fill="var(--navy)"/>
          <rect x="7.5" y="9.5" width="13" height="9" fill="none" stroke="#fff" stroke-width="1.2"/>
          <path d="M7.5 9.5 L14 15 L20.5 9.5 M7.5 18.5 L12 14 M20.5 18.5 L16 14" fill="none" stroke="#fff" stroke-width="1.2"/>
        </svg>
        <span>drmarlena@lumoraclinic.example</span>
      </li>
      <li class="contact-list__item">
        <svg class="contact-list__icon" viewBox="0 0 28 28" aria-hidden="true">
          <circle cx="14" cy="14" r="14" fill="var(--navy)"/>
          <g fill="none" stroke="#fff" stroke-width="1.1">
            <circle cx="14" cy="14" r="6.5"/>
            <ellipse cx="14" cy="14" rx="2.8" ry="6.5"/>
            <path d="M7.5 14 H20.5 M8.5 10.8 H19.5 M8.5 17.2 H19.5"/>
          </g>
        </svg>
        <span>lumoraclinic.example</span>
      </li>
    </ul>
  </section>

</main>
</body>
</html>
```